Photo Storage Service - Web Application

This is web design for a simple photo storage service.
There is a web page and on the left side is a list of folders and on the right side there are photo thumbnails. By pressing a photo thumbnail, they will see the full size (it's just a link to a different page).
This project is limited only to ONE page, which is the page with the folders list and the thumbnails. However it contains some features that I will try to list here:
- Name of the service: Tavo Vault
- Location of account: http://username.tavo.example
- Folder list: Show all folders belonging to the user. Because you have to be able to drag photos to a folder, they have to be visible and cannot be hidden behind a menu item etc.
- Thumbnails with photos (in the future also videos)
- Adjusted view with smaller thumbnails and less space for folder list (so it is possible to view a larger quantity of thumbnails)- Select multiple thumbnails with rectangle- Show that a thumbnail is selected (maybe bold border?)
- Simple mobile view, but no emphasis on the mobile view in this design project.
- Drag one or more selected photos to a folder
- Delete one or more selected photos
- Drag a folder to another folder
- Rename folder
- Delete folder
- Create folder
- Show progress when deleting/moving (because it calls for every photo, so if there are 100 photos, it will delete 1 by 1 and it will take about 10 seconds - you could show progress bar or equivalent)
Background information: This is for a photo storage service NOT intended for sharing photos, but intended to indefinitely store photos and for yourself to browse your own photos.
It is a design requirement that it loads extremely fast. So we need to limit as much as possible extra graphics that cannot be done by CSS and other external libraries.
(I know this is ONLY design and nothing to do with CSS or libraries, but I can assess from the design if it might be heavy to load when implemented)
I have attached a crude screenshot of the current design, just for your understanding. It should not match this design and you are not in any way supposed to FIT your design into this same style or structure.
Target Market(s)
Consumers
Number of Pages Required
1 page
Font styles to use
Look and feel
Each slider illustrates characteristics of the customer's brand and the style your logo design should communicate.

```html
<!DOCTYPE html>
<html lang="en">
<head>
<meta charset="utf-8">
<title>Tavo Vault</title>
<link rel="stylesheet" href="https://fonts.googleapis.com/css2?family=Montserrat:wght@400;500&display=swap">
<style>
:root{
  --teal:#0bb592;
  --teal-light:#17bc9c;
  --dark:#2f2f2f;
  --ink:#2a2a2a;
  --side:#f6f7f7;
  --muted:#7c7c7c;
  --faint:#c8c8c8;
  --white:#ffffff;
}
*{margin:0;padding:0;box-sizing:border-box}
html,body{width:1200px;height:750px;overflow:hidden}
body{font-family:'Montserrat',sans-serif;background:var(--dark);position:relative}
.abs{position:absolute}
.topbar{left:0;top:0;width:1200px;height:51px;background:var(--teal)}
.brand-area{left:0;top:0;width:266px;height:51px;background:var(--teal-light)}
.brand{left:48px;top:14px;color:var(--white);font-size:17px;font-weight:400}
.sidebar{left:0;top:51px;width:266px;height:699px;background:linear-gradient(90deg,#fafafa,#f2f3f3)}
.create-btn{left:48px;top:76px;width:115px;height:31px;border-radius:16px;background:var(--teal);color:var(--white);font-size:12.5px;display:flex;align-items:center;justify-content:center;gap:6px;box-shadow:0 2px 5px rgba(0,0,0,.15)}
.create-btn b{font-weight:400;font-size:16px;line-height:1}
.folder{left:64px;font-size:10.5px;color:var(--muted);height:16px;line-height:16px}
.folder-pill{left:48px;width:197px;height:30px;border-radius:15px}
.folder-pill.active{top:130px;background:var(--ink)}
.folder-pill.hover{top:254px;background:#e5e6e6}
.dots{width:3px;height:12px;display:flex;flex-direction:column;justify-content:space-between}
.dots i{display:block;width:3px;height:3px;border-radius:50%;background:var(--white)}
.dots.pale i{background:#c9c9c9}
.menu{left:132px;top:153px;width:98px;height:59px;background:var(--white);box-shadow:0 2px 8px rgba(0,0,0,.15);font-size:8.5px}
.menu div{height:29.5px;line-height:29.5px;padding-left:14px;color:var(--ink)}
.menu div+div{border-top:1px solid #eee;color:var(--muted);padding-left:18px}
.tool{top:82px;font-size:8.5px;color:#b9b9b9;display:flex;align-items:center;gap:6px}
.avatar{left:950px;top:9px;width:32px;height:32px;border-radius:50%;background:linear-gradient(135deg,#8a6a55,#d9cfc6)}
.user{left:987px;top:18px;color:var(--white);font-size:11px}
.user-menu{left:986px;top:37px;width:92px;height:56px;font-size:8.5px;box-shadow:0 2px 6px rgba(0,0,0,.2)}
.user-menu div{height:28px;line-height:28px;text-align:center}
.user-menu .profile{background:var(--white);color:var(--muted)}
.user-menu .signout{background:var(--teal);color:var(--white)}
.thumb{width:144px;height:138px}
.thumb.sel{outline:1px solid #35c9a7}
.play{left:50%;top:50%;width:22px;height:22px;margin:-11px 0 0 -11px;border:1.5px solid rgba(255,255,255,.9);border-radius:50%}
.play::after{content:"";position:absolute;left:7px;top:5px;border-left:8px solid #fff;border-top:5px solid transparent;border-bottom:5px solid transparent}
.selection{left:318px;top:114px;width:443px;height:316px;border:1px dashed #d5d5d5;background:rgba(125,125,125,.42)}
.upload{left:284px;top:454px;width:307px;height:203px;background:var(--white)}
.upload-btn{left:79px;top:101px;width:149px;height:31px;border-radius:16px;background:var(--teal);color:var(--white);font-size:10.5px;display:flex;align-items:center;justify-content:center}
.upload-hint{left:0;top:146px;width:307px;text-align:center;font-size:10px;color:var(--faint)}
.submit{left:386px;top:681px;width:105px;height:31px;border-radius:16px;background:var(--white);color:var(--ink);font-size:12px;display:flex;align-items:center;justify-content:center}
</style>
</head>
<body>
<header class="abs topbar"></header>
<div class="abs brand-area"></div>
<div class="abs brand">Tavo Vault</div>

<div class="abs avatar" role="img" aria-label="User profile photo"></div>
<div class="abs user">Lena Hartwell</div>
<div class="abs dots" style="left:1076px;top:19px"><i></i><i></i><i></i></div>
<div class="abs user-menu"><div class="profile">Profile</div><div class="signout">Signout</div></div>

<aside class="abs sidebar"></aside>
<div class="abs create-btn"><b>+</b> Create Folder</div>

<div class="abs folder-pill active"></div>
<div class="abs folder-pill hover"></div>
<div class="abs folder" style="top:135px;color:#fff">Inbox</div>
<div class="abs dots" style="left:226px;top:139px"><i></i><i></i><i></i></div>
<div class="abs dots pale" style="left:226px;top:263px"><i></i><i></i><i></i></div>
<div class="abs folder" style="top:167px">80,s party</div>
<div class="abs folder" style="top:198px">A day in Oslo</div>
<div class="abs folder" style="top:229px">A Tour of Svendborg</div>
<div class="abs folder" style="top:261px;color:#555">Alicante 2017</div>
<div class="abs folder" style="top:292px">Bandardan</div>
<div class="abs folder" style="top:323px">Brazil</div>
<div class="abs folder" style="top:354px">Random</div>
<div class="abs folder" style="top:386px">Thailand 1</div>
<div class="abs folder" style="top:417px">Thailand 2</div>
<div class="abs folder" style="top:448px">Usa</div>
<div class="abs folder" style="top:479px">Thumbnails</div>
<div class="abs folder" style="top:511px">Videos/thumbnails</div>
<div class="abs menu"><div>Rename Folder</div><div>Delete Folder</div></div>

<div class="abs tool" style="left:287px">
  <svg width="14" height="17" viewBox="0 0 14 17" fill="none" stroke="#17bc9c" stroke-width="1.2"><path d="M1 3h12M5 3V1h4v2M2.5 3l1 13h7l1-13M5.5 6v8M8.5 6v8"/></svg>
  Delete Select Files
</div>
<div class="abs tool" style="left:432px">
  <svg width="18" height="18" viewBox="0 0 18 18" fill="none" stroke="#17bc9c" stroke-width="1.2"><rect x="1" y="1" width="10" height="10" stroke-dasharray="2 1.5"/><rect x="7" y="7" width="10" height="10"/><path d="M4 4l8 8M12 8v4H8"/></svg>
  Drag files to the destined folder
</div>

<div class="abs thumb sel" style="left:284px;top:128px;background:linear-gradient(135deg,#b77a45,#e9cfc0)" role="img" aria-label="Girl holding a carved pumpkin"><span class="abs play"></span></div>
<div class="abs thumb sel" style="left:447px;top:128px;background:linear-gradient(135deg,#7c7d58,#a49c78)" role="img" aria-label="Woman lying in grass"></div>
<div class="abs thumb sel" style="left:610px;top:128px;background:linear-gradient(135deg,#d8c9b6,#7d6b68)" role="img" aria-label="Couple sitting together at sunset"></div>
<div class="abs thumb" style="left:772px;top:128px;background:linear-gradient(180deg,#e8d8c4,#c7a98a)" role="img" aria-label="Two children on a beach"></div>
<div class="abs thumb" style="left:934px;top:128px;background:linear-gradient(135deg,#c9bdb3,#4a4442)" role="img" aria-label="Hands holding a camera lens"></div>
<div class="abs thumb sel" style="left:284px;top:285px;background:linear-gradient(135deg,#d9dde2,#9b7d63)" role="img" aria-label="Woman in sunglasses in a field"></div>
<div class="abs thumb sel" style="left:447px;top:285px;background:linear-gradient(180deg,#b8c8d9,#6f8ea4)" role="img" aria-label="Rusted shipwreck at sea"></div>
<div class="abs thumb sel" style="left:610px;top:285px;background:linear-gradient(180deg,#c9c9c6,#8e8c86)" role="img" aria-label="Three friends sitting on steps"></div>
<div class="abs thumb" style="left:772px;top:285px;background:linear-gradient(180deg,#6e6f7e,#e1b48a)" role="img" aria-label="Dancers at sunset"><span class="abs play"></span></div>
<div class="abs thumb" style="left:934px;top:285px;background:linear-gradient(135deg,#2a2220,#c9242a)" role="img" aria-label="Child in a costume with a mask"></div>

<div class="abs selection"></div>
<svg class="abs" style="left:759px;top:428px" width="10" height="14" viewBox="0 0 10 14"><path d="M1 1v11l3-3 2 4 1.5-.7-2-4H9z" fill="#fff" stroke="#222" stroke-width=".8"/></svg>

<section class="abs upload">
  <svg class="abs" style="left:124px;top:40px" width="60" height="46" viewBox="0 0 60 46"><path d="M14 44a12 12 0 0 1-1-24 17 17 0 0 1 32-4 13 13 0 0 1 2 28z" fill="#c4c4c4"/><path d="M30 17l-10 11h6v12h8V28h6z" fill="#fff"/></svg>
  <div class="abs upload-btn">Choose files to upload</div>
  <div class="abs upload-hint">Drag and drop files here to upload</div>
</section>
<div class="abs submit">Submit</div>
</body>
</html>
```